****FLYER design - LAW FIRM ADVERTISEMENT****

We are a small law firm based in Los Angeles, CA. We need an flyer used for advertising that we will be passing out. We want the flyer to be about 4in x 6in.

We want the flyer to advertise the name of our firm: MORVANTE KELDRIC LLP (no period)
- We want our group photo to take up a good portion of the flyer (although it's okay if parts of the photo have wording over it.)

COLORS: Our firm colors are different shades of steal/metal grey with a bit of a bold orange accent. Any bold writing, like our slogan, names of practice areas,... should be in orange.

We envision a horizontal lay-out of the flyer, but are open to creative options laid out vertically!

Feel free to play with the fonts, the sizing, the color combinations,...

We want the flyer to advertise our two areas of practice: PERSONAL INJURY and EMPLOYMENT LAW. Please also place each photo icon of our areas of practice somewhere around the name (ambulance photo for personal injury; person behind computer desk for employment law). The icons can be relatively small.

Under Personal Injury, please write:
If you or a loved one are suffering from an injury or wrongful death caused by the careless or intentional acts of others, then you have the right to pursue compensation for your injury, out-of-pocket expenses, lost wages, emotional anguish, and more.

Under Employment Law, please write:
Our attorneys regularly represent clients in disputes involving sex, age and race discrimination, sexual harassment, retaliatory discharge, defamation, unlawful termination, breach of employment contracts, and more.

Somewhere on the flyer, please write our slogan IN ITALICS (and probably in orange):
- You Speak. We Listen. They Pay.

In somewhat bright and bold writing, please write "CONTACT US FOR A FREE CONSULTATION TODAY!" (maybe just after our slogan?)
- And under that phrase, write:
- 731 W. Larkmoor Avenue, Suite 400 Glenfield, CA 90488
phone: 555.318.9062
fax: 555.318.9074
email: info@mkrlegal-example.com
web: www.mkrlegal-example.com

If possible, and only if there's room without it looking too busy, somewhere in the upper left corner, place our "MKR" logo.
Updates

PLEASE NOTE THAT WE CHANGED OUR GROUP PHOTO TO A SLIGHTLY EDITED ONE.  PLEASE BE SURE TO USE THE NEW ONE!!!  (We deleted the old.)

Target Market(s)

employees, lower and mid-income individuals, minority communities. However, we still want the flyer to look sleek, modern, and professional.

Industry/Entity Type

Advertising

Requirements
Must have
• Firm Name,
Photo of Partners,
Names, photos, and small description of practice areas,
Firm slogan,
"Contact us for a free consultation today!",
Firm contact info.

And only if space and overall look permits, firm "MKR" logo.

We want an overall very sleek, modern feel to our flyer. While we do want to look professional, we wanted a more approachable feel than the typical, conservative law offices.
Nice to have
• Firm "MKR" logo

Horizontal lay out, though we're open to vertical options.

```html
<!DOCTYPE html>
<html lang="en">
<head>
<meta charset="utf-8">
<title>Morvante Keldric LLP – Flyer</title>
<link rel="stylesheet" href="https://fonts.googleapis.com/css2?family=Fira+Sans:ital,wght@0,500;0,600;0,700;1,700&family=Fira+Sans+Condensed:wght@500;600&display=swap">
<style>
  :root {
    --page-bg: #ffffff;
    --slate: #5b6671;
    --slate-text: #5e6a76;
    --silver-light: #e6e7e9;
    --silver-mid: #c9cbce;
    --silver-dark: #b1b4b8;
    --orange: #e17a1c;
    --ink: #111111;
    --white: #ffffff;
    --name-light: #f2f3f4;
    --name-dark: #c9ced3;
  }
  * { box-sizing: border-box; margin: 0; padding: 0; }
  html, body {
    width: 1200px; height: 1200px; overflow: hidden;
    background: var(--page-bg);
  }
  .flyer {
    position: absolute; left: 50px; top: 233px;
    width: 1100px; height: 733px;
    background: var(--white);
    border: 1px solid #d4d6d8;
    overflow: hidden;
  }
  .name-band {
    position: absolute; left: 0; top: 0;
    width: 667px; height: 124px;
    background: var(--slate);
    display: flex; align-items: center; justify-content: center;
  }
  .firm-name {
    font-family: "Fira Sans", sans-serif;
    font-weight: 700; font-size: 47px; letter-spacing: -0.5px;
    color: var(--name-light);
    white-space: nowrap;
  }
  .team-photo {
    position: absolute; left: 0; top: 124px;
    width: 667px; height: 347px;
    background: linear-gradient(100deg, #b79a78 0%, #6f5a44 30%, #d9d3cc 50%, #8d6a3e 75%, #4a3a26 100%);
  }
  .contact-panel {
    position: absolute; left: 667px; top: 0;
    width: 433px; height: 471px;
    background: linear-gradient(150deg, var(--silver-light) 0%, var(--silver-mid) 55%, var(--silver-dark) 100%);
    padding: 44px 0 0 44px;
  }
  .slogan {
    font-family: "Fira Sans", sans-serif;
    font-style: italic; font-weight: 700;
    font-size: 43px; line-height: 47px;
    color: var(--orange);
    text-transform: uppercase;
  }
  .cta {
    margin-top: 22px;
    font-family: "Fira Sans Condensed", sans-serif;
    font-weight: 600; font-size: 33px; line-height: 34px;
    color: var(--slate-text);
  }
  .address {
    margin-top: 24px;
    font-family: "Fira Sans Condensed", sans-serif;
    font-weight: 500; font-size: 21px; line-height: 24.5px;
    color: var(--slate-text);
    font-style: normal;
  }
  .practice {
    position: absolute; top: 498px;
    display: flex; gap: 14px;
  }
  .practice--injury { left: 50px; width: 490px; }
  .practice--employment { left: 572px; width: 500px; }
  .practice-icon {
    flex: none; width: 81px; height: 81px;
    background: var(--ink);
    border: 3px solid var(--orange);
    border-radius: 8px;
    display: flex; align-items: center; justify-content: center;
  }
  .practice-title {
    font-family: "Fira Sans Condensed", sans-serif;
    font-weight: 600; font-size: 37px; line-height: 38px;
    color: var(--orange);
    margin-top: -4px;
  }
  .practice-text {
    margin-top: 4px;
    font-family: "Fira Sans Condensed", sans-serif;
    font-weight: 600; font-size: 18px; line-height: 23.5px;
    color: var(--slate-text);
  }
</style>
</head>
<body>
  <main class="flyer">
    <header class="name-band">
      <h1 class="firm-name">MORVANTE KELDRIC LLP</h1>
    </header>

    <div class="team-photo" role="img" aria-label="Group photo of the firm's three partners standing in an elegant office lobby"></div>

    <section class="contact-panel">
      <p class="slogan">You speak.<br>We listen.<br>They pay.</p>
      <p class="cta">Contact us for a free<br>consultation today</p>
      <address class="address">
        731 W. Larkmoor Avenue,<br>
        Suite 400 Glenfield, CA 90488<br>
        phone: 555.318.9062<br>
        fax: 555.318.9074<br>
        email: info@mkrlegal-example.com<br>
        web: www.mkrlegal-example.com
      </address>
    </section>

    <section class="practice practice--injury">
      <div class="practice-icon">
        <svg width="58" height="40" viewBox="0 0 58 40" aria-hidden="true">
          <path d="M2 6h34v26H2z M36 14h11l9 10v8H36z" fill="#fff"/>
          <path d="M39 17h7l6 7H39z" fill="#111"/>
          <path d="M16 11h6v6h6v6h-6v6h-6v-6h-6v-6h6z" fill="#111"/>
          <circle cx="13" cy="33" r="5" fill="#fff" stroke="#111" stroke-width="2"/>
          <circle cx="45" cy="33" r="5" fill="#fff" stroke="#111" stroke-width="2"/>
        </svg>
      </div>
      <div>
        <h2 class="practice-title">PERSONAL INJURY</h2>
        <p class="practice-text">If you or a loved one are suffering from an<br>injury or wrongful death caused by the<br>careless or intentional acts of others, then<br>you have the right to pursue compensation<br>for your injury, out-of-pocket expenses, lost<br>wages, emotional anguish, and more.</p>
      </div>
    </section>

    <section class="practice practice--employment">
      <div class="practice-icon">
        <svg width="50" height="52" viewBox="0 0 50 52" aria-hidden="true">
          <circle cx="18" cy="9" r="6" fill="#fff"/>
          <path d="M12 17h11l3 12h-8l3 12h-4l-4-10h-3z" fill="#fff"/>
          <rect x="27" y="12" width="14" height="11" fill="#fff"/>
          <rect x="24" y="25" width="24" height="4" fill="#fff"/>
          <rect x="42" y="29" width="3" height="20" fill="#fff"/>
          <path d="M4 30h12v4H8v15H5z" fill="#fff"/>
        </svg>
      </div>
      <div>
        <h2 class="practice-title">EMPLOYMENT LAW</h2>
        <p class="practice-text">Our attorneys regularly represent clients<br>in disputes involving sex, age and race<br>discrimination, sexual harassment, retaliatory<br>discharge, defamation, unlawful termination,<br>breach of employment contracts, and more.</p>
      </div>
    </section>
  </main>
</body>
</html>
```